Offshore Energy Projects Management Consultancy needs a business card design

Logo available. We provide teams to deliver engineering consultancy, project management and delivery teams mainly in the offshore renewables sector. The company is all about bringing the right people to a project to deliver the scope.

The business card will be used for all staff.

The business card should be quite simple, vibrant and uncluttered but convey experience, enthusiasm and integration.

Target Market(s)

Energy Project Developers and Tier 1 construction companies

Contact Information for Business Card

Logo should be on the back of the card. I'm happy for the designer to play with the colour of the logo and background colour.

Front of the card should convey all the must have information in a clear and professional manner but without being overly traditional.

Colors

Designer to choose colors to be used in the design.

Requirements
Must have
• Land Line Tel Number, Mobile Tel Number, Email, business address, web address.

```html
<!DOCTYPE html>
<html lang="en">
<head>
<meta charset="utf-8">
<title>Tidewell Delivery Group – Business Card</title>
<link rel="stylesheet" href="https://fonts.googleapis.com/css2?family=Arimo:wght@400;700&family=Carlito&display=swap">
<style>
  :root {
    --stage: #5e5e5e;
    --card-light: #e6e6e2;
    --card-dark: #1f2222;
    --brand-blue: #1277c2;
    --ink: #1e1e1e;
    --ghost: rgba(150, 150, 145, 0.16);
    --rule: #222;
  }
  * { margin: 0; padding: 0; box-sizing: border-box; }
  html, body { width: 907px; height: 1200px; overflow: hidden; }
  body { background: var(--stage); position: relative; font-family: "Arimo", Arial, sans-serif; }

  .card {
    position: absolute;
    left: 42px;
    width: 821px;
    height: 529px;
    border-radius: 6px 28px 0 20px;
    overflow: hidden;
  }
  .card--front { top: 42px; background: var(--card-light); }
  .card--back { top: 622px; background: var(--card-dark); }

  .card__swoosh { position: absolute; inset: 0; width: 100%; height: 100%; }

  .front__ghost-initials {
    position: absolute;
    left: 40px; top: 74px;
    font-family: "Arimo", Arial, sans-serif;
    font-weight: 700;
    font-size: 350px;
    color: var(--ghost);
    white-space: nowrap;
    line-height: 1;
  }
  .front__brand {
    position: absolute;
    left: 34px; top: 262px;
    font-weight: 700;
    font-size: 38px;
    color: var(--brand-blue);
    letter-spacing: 1px;
  }
  .front__divider {
    position: absolute;
    left: 258px; top: 153px;
    width: 1px; height: 239px;
    background: var(--rule);
  }
  .person {
    position: absolute;
    right: 51px; top: 86px;
    text-align: right;
  }
  .person__name {
    font-family: "Carlito", Calibri, sans-serif;
    font-weight: 400;
    font-size: 44px;
    color: var(--brand-blue);
    line-height: 1;
  }
  .person__role {
    font-size: 19px;
    color: var(--ink);
    margin-top: 6px;
  }

  .contact-list { list-style: none; }
  .contact-list__item {
    position: absolute;
    left: 273px;
    height: 24px;
    display: flex;
    align-items: center;
    font-size: 19px;
    color: var(--ink);
    white-space: nowrap;
  }
  .contact-list__icon { width: 20px; height: 20px; margin-right: 25px; flex: none; fill: var(--ink); }
  .contact-list__icon--outline { fill: none; stroke: var(--ink); stroke-width: 1.6; }

  .back__brand {
    position: absolute;
    left: 0; right: 0; top: 290px;
    text-align: center;
    font-weight: 700;
    font-size: 38px;
    letter-spacing: 1px;
    color: var(--brand-blue);
  }
</style>
</head>
<body>

<section class="card card--front">
  <div class="front__ghost-initials" aria-hidden="true">TDG</div>
  <svg class="card__swoosh" viewBox="0 0 821 529" preserveAspectRatio="none" aria-hidden="true">
    <path d="M821 407 C 770 500 640 525 522 529 L 821 529 Z" fill="var(--brand-blue)"/>
  </svg>

  <div class="front__brand">TIDEWELL</div>
  <div class="front__divider"></div>

  <div class="person">
    <h1 class="person__name">Daniel Reyes</h1>
    <p class="person__role">Founder</p>
  </div>

  <ul class="contact-list">
    <li class="contact-list__item" style="top:177px">
      <svg class="contact-list__icon" viewBox="0 0 24 24"><path d="M6.6 10.8c1.4 2.8 3.8 5.1 6.6 6.6l2.2-2.2c.3-.3.7-.4 1-.2 1.1.4 2.3.6 3.6.6.6 0 1 .4 1 1V20c0 .6-.4 1-1 1C10.6 21 3 13.4 3 4c0-.6.4-1 1-1h3.5c.6 0 1 .4 1 1 0 1.3.2 2.5.6 3.6.1.3 0 .7-.2 1L6.6 10.8z"/></svg>
      <span>0198765432</span>
    </li>
    <li class="contact-list__item" style="top:220px">
      <svg class="contact-list__icon" viewBox="0 0 24 24"><path d="M7 1h10a2 2 0 0 1 2 2v18a2 2 0 0 1-2 2H7a2 2 0 0 1-2-2V3a2 2 0 0 1 2-2zm0 3v15h10V4H7zm5 16a1 1 0 1 0 0 2 1 1 0 0 0 0-2z"/></svg>
      <span>0987654321</span>
    </li>
    <li class="contact-list__item" style="top:260px">
      <svg class="contact-list__icon" viewBox="0 0 24 24"><path d="M2 5h20v14H2V5zm2 2v.5l8 5 8-5V7H4z"/></svg>
      <span>TIDEWELL.DELIVERY.GROUP@MAIL.COM</span>
    </li>
    <li class="contact-list__item" style="top:300px">
      <svg class="contact-list__icon" viewBox="0 0 24 24"><path d="M12 1a8 8 0 0 0-8 8c0 6 8 14 8 14s8-8 8-14a8 8 0 0 0-8-8zm0 11a3 3 0 1 1 0-6 3 3 0 0 1 0 6z"/></svg>
      <span>45, HARBOUR LANE</span>
    </li>
    <li class="contact-list__item" style="top:341px">
      <svg class="contact-list__icon contact-list__icon--outline" viewBox="0 0 24 24"><circle cx="12" cy="12" r="9.5"/><ellipse cx="12" cy="12" rx="4" ry="9.5"/><path d="M2.5 12h19M4 7h16M4 17h16"/></svg>
      <span>WWW.TIDEWELLDELIVERYGROUP.CO.IN</span>
    </li>
  </ul>
</section>

<section class="card card--back">
  <svg class="card__swoosh" viewBox="0 0 821 529" preserveAspectRatio="none" aria-hidden="true">
    <path d="M821 407 C 770 500 640 525 522 529 L 821 529 Z" fill="var(--brand-blue)"/>
  </svg>
  <div class="back__brand">TIDEWELL DELIVERY GROUP</div>
</section>

</body>
</html>
```